Unique Flyer Project - www.plumorchardpanel.com.au

The purpose of this flyer is trying to get recipients to visit the website www.plumorchardpanel.com.au and sign up to the offer. I need it to be simple/to the point, eye catching and professional. I will post up a basic idea I have but feel free to put your own spin on it if you think you have great ideas to get people to visit the site, if not then just improve upon the quality of mine and make it look like a respected company.

I also think a red band or something that REALLY catches the eye highlighting one of the important aspects of the flyer (the domain?) could be great so even if someone is about to put it in the bin, the popping red-on-white-background catches their eye so they end up looking at and reading the flyer.

I would also love a VERY SIMPLE design for the backside of the flyer, just a red box/band (whatever you think is good) with the domain 'www.plumorchardpanel.com.au' in it. NOTHING ELSE! Just so if it's floating around the table and it's upside down, there's something eye catching that might entice the householder to look at it.

DESIGN IS FOR DL FLYER: 99mm X 210mm

Target Market(s)

Australian Residents interested in earning money from home.

Industry/Entity Type

It Company

Requirements
Must have
• Eye catching (mainly red band/box/bar on front & back page), SIMPLE, elegant/professional.
Should not have
• ANYTHING unnecessary to the reader that will distract them from the ultimate point - GET PAID TO DO SURVEYS FROM YOUR OWN HOME ON THE COMPUTER!

```html
<!DOCTYPE html>
<html lang="en">
<head>
<meta charset="utf-8">
<title>Plum Orchard Panel – Flyer</title>
<link rel="stylesheet" href="https://fonts.googleapis.com/css2?family=Roboto+Condensed:wght@400;700;800&display=swap">
<style>
  :root {
    --ink: #111111;
    --brand-blue: #1f62c9;
    --accent-red: #d3140f;
    --band-red-dark: #8e0806;
    --band-red-light: #e4231c;
    --paper: #ffffff;
    --frame: #3a3a3a;
    --flag-navy: #0b2a7a;
    --cash-green: #a9b89a;
    --cash-dark: #6f7f62;
    --illus-red: #d9391f;
    --illus-skin: #e8b89a;
  }
  * { margin: 0; padding: 0; box-sizing: border-box; }
  html, body { width: 1200px; height: 566px; overflow: hidden; background: var(--paper); }
  .flyer {
    position: relative;
    width: 1200px;
    height: 566px;
    background: var(--paper);
    border: 2px solid var(--frame);
    overflow: hidden;
    font-family: "Roboto Condensed", "Arial Narrow", sans-serif;
    color: var(--ink);
  }
  .brand-name {
    position: absolute;
    left: 280px;
    top: 48px;
    width: 440px;
    font-weight: 800;
    color: var(--brand-blue);
    font-size: 66px;
    line-height: 1;
    text-transform: uppercase;
    text-align: center;
    white-space: nowrap;
    letter-spacing: -0.5px;
  }
  .brand-illustration {
    position: absolute;
    left: 725px;
    top: 45px;
    width: 150px;
    height: 160px;
    border-radius: 10px;
    background: linear-gradient(160deg, var(--illus-skin) 0%, var(--illus-red) 55%, #5a4a3e 100%);
  }
  .country-flag {
    position: absolute;
    left: 1008px;
    top: 28px;
    width: 157px;
    height: 92px;
    background: var(--flag-navy);
  }
  .availability {
    position: absolute;
    left: 990px;
    top: 126px;
    width: 194px;
    text-align: center;
    font-size: 25px;
    line-height: 1.15;
    text-transform: uppercase;
  }
  .availability strong { font-weight: 700; }
  .headline {
    position: absolute;
    left: 0;
    top: 228px;
    width: 100%;
    text-align: center;
    font-weight: 400;
    font-size: 54px;
  }
  .earnings {
    position: absolute;
    left: 0;
    top: 316px;
    width: 100%;
    text-align: center;
    font-weight: 700;
    font-size: 36px;
  }
  .earnings .amount { color: var(--accent-red); font-size: 58px; vertical-align: -4px; }
  .flexibility {
    position: absolute;
    left: 0;
    top: 386px;
    width: 100%;
    text-align: center;
    font-weight: 400;
    font-size: 40px;
  }
  .domain-band {
    position: absolute;
    left: 0;
    top: 440px;
    width: 100%;
    height: 124px;
    background: linear-gradient(90deg, var(--band-red-dark) 0%, var(--band-red-light) 50%, var(--band-red-dark) 100%);
    display: flex;
    align-items: center;
    justify-content: center;
  }
  .domain {
    color: var(--paper);
    font-size: 46px;
    font-weight: 400;
    letter-spacing: 0.5px;
  }
  .cash-stack {
    position: absolute;
    border-radius: 6px;
    background: linear-gradient(135deg, var(--cash-green) 0%, #d9e2cd 45%, var(--cash-dark) 100%);
  }
  .cash-stack--left { left: -10px; top: 380px; width: 252px; height: 200px; clip-path: polygon(0 8%, 55% 0, 100% 22%, 96% 100%, 0 100%); }
  .cash-stack--right { left: 948px; top: 372px; width: 264px; height: 210px; clip-path: polygon(10% 14%, 70% 0, 100% 6%, 100% 100%, 0 100%, 4% 40%); }
</style>
</head>
<body>
<main class="flyer">
  <div class="brand-name">Plum Orchard<br>Panel</div>
  <div class="brand-illustration" role="img" aria-label="Illustration of a woman in a red top lying down using a laptop"></div>

  <div class="country-flag" role="img" aria-label="Flag of Australia"></div>
  <p class="availability">Now open to<br>residents of<br><strong>Australia</strong></p>

  <h1 class="headline">Could You Use An Extra Income?</h1>
  <p class="earnings">Earn as much as <span class="amount">$50</span> per survey!</p>
  <p class="flexibility">Work from home and choose your hours!</p>

  <div class="domain-band">
    <span class="domain">www.plumorchardpanel.com.au</span>
  </div>

  <div class="cash-stack cash-stack--left" role="img" aria-label="Photograph of stacked bundles of banknotes"></div>
  <div class="cash-stack cash-stack--right" role="img" aria-label="Photograph of stacked bundles of banknotes"></div>
</main>
</body>
</html>
```